Kestrel Gardenworks Business Card

An eye catching, yet simple business card that includes;

1. our logo
2. office phone - 5083172946
3. email - kestrelgardenworks@mailbrook.com
4. website - www.kestrelgardenworks.com
5. instagram - @kestrelgardenworksnv

```html
<!DOCTYPE html>
<html lang="en">
<head>
<meta charset="utf-8">
<title>Kestrel Gardenworks Business Card</title>
<link rel="stylesheet" href="https://fonts.googleapis.com/css2?family=Montserrat:wght@400;500;800&display=swap">
<style>
  :root {
    --backdrop: #3b3b3b;
    --ink: #1e1e1e;
    --paper: #ffffff;
    --copper: #b5621f;
    --rule: #6a6a6a;
  }
  * { margin: 0; padding: 0; box-sizing: border-box; }
  html, body { width: 1200px; height: 1200px; overflow: hidden; }
  body {
    background: var(--backdrop);
    font-family: "Montserrat", sans-serif;
    position: relative;
  }
  .card {
    position: absolute;
    left: 170px;
    width: 860px;
    height: 491px;
    border-radius: 34px;
    overflow: hidden;
    box-shadow: 0 4px 0 var(--copper), 0 16px 30px rgba(0,0,0,.45);
  }
  .card--front { top: 70px; background: var(--paper); }
  .card--back { top: 630px; background: var(--ink); }
  .card__shape { position: absolute; inset: 0; }
  .brand {
    position: absolute;
    display: flex;
    align-items: center;
    gap: 16px;
    font-weight: 800;
    color: var(--copper);
    white-space: nowrap;
  }
  .brand__dot {
    flex: none;
    border-radius: 50%;
    border: 6px solid var(--copper);
  }
  .card--front .brand { left: 110px; top: 62px; font-size: 42px; }
  .card--front .brand__dot { width: 50px; height: 50px; }
  .card--back .brand { left: 0; right: 0; top: 200px; justify-content: center; font-size: 54px; }
  .card--back .brand__dot { width: 62px; height: 62px; }
  .person { position: absolute; left: 92px; top: 378px; }
  .person__name { color: var(--copper); font-size: 38px; font-weight: 400; letter-spacing: -1px; line-height: 1; }
  .person__title { color: var(--paper); font-size: 22px; font-weight: 400; margin-top: 4px; }
  .divider { position: absolute; left: 470px; top: 280px; width: 1px; height: 170px; background: var(--rule); }
  .contacts { position: absolute; left: 505px; top: 268px; list-style: none; }
  .contacts li {
    display: flex; align-items: center; gap: 12px;
    color: var(--paper); font-size: 15px; font-weight: 500;
    height: 38px;
  }
  .contacts svg { width: 22px; height: 22px; flex: none; }
  .contacts li:first-child { font-size: 19px; }
</style>
</head>
<body>

<section class="card card--front" aria-label="Business card front">
  <svg class="card__shape" viewBox="0 0 860 491" preserveAspectRatio="none" aria-hidden="true">
    <path d="M0,345 C300,260 600,165 860,135 L860,491 L0,491 Z" fill="var(--copper)"/>
    <path d="M0,353 C300,268 600,173 860,143 L860,491 L0,491 Z" fill="var(--ink)"/>
  </svg>
  <div class="brand"><span class="brand__dot"></span>Kestrel Gardenworks</div>
  <div class="person">
    <p class="person__name">FULL NAME</p>
    <p class="person__title">TITLE</p>
  </div>
  <div class="divider"></div>
  <ul class="contacts">
    <li>
      <svg viewBox="0 0 24 24"><path fill="var(--copper)" d="M6.6 10.8a15.1 15.1 0 0 0 6.6 6.6l2.2-2.2a1 1 0 0 1 1-.25 11.4 11.4 0 0 0 3.6.57 1 1 0 0 1 1 1V20a1 1 0 0 1-1 1A17 17 0 0 1 3 4a1 1 0 0 1 1-1h3.5a1 1 0 0 1 1 1c0 1.25.2 2.450.57 3.57a1 1 0 0 1-.25 1z"/></svg>
      5083172946
    </li>
    <li>
      <svg viewBox="0 0 24 24"><rect x="2" y="5" width="20" height="14" rx="1" fill="none" stroke="var(--copper)" stroke-width="2"/><path d="M2 6l10 7 10-7" fill="none" stroke="var(--copper)" stroke-width="2"/></svg>
      kestrelgardenworks@mailbrook.com
    </li>
    <li>
      <svg viewBox="0 0 24 24" fill="none" stroke="var(--copper)" stroke-width="1.8"><circle cx="12" cy="12" r="9.5"/><ellipse cx="12" cy="12" rx="4.2" ry="9.5"/><path d="M2.5 12h19M4 7h16M4 17h16"/></svg>
      www.kestrelgardenworks.com
    </li>
    <li>
      <svg viewBox="0 0 24 24"><rect x="3" y="3" width="18" height="18" rx="4" fill="none" stroke="var(--copper)" stroke-width="2"/></svg>
      @kestrelgardenworksnv
    </li>
  </ul>
</section>

<section class="card card--back" aria-label="Business card back">
  <div class="brand"><span class="brand__dot"></span>Kestrel Gardenworks</div>
</section>

</body>
</html>
```